Stonegate Towing Business Card

Towing
Accident towing
Mechanical breakdown
Insurance, salvage and recovery
4wd off road towing
Light & Heavy towing
7354 2618
24 hour business 7 days

Logo can be whole size on front

Industry/Entity Type

Towing/ transport

Contact Information for Business Card

The above

```html
<!DOCTYPE html>
<html lang="en">
<head>
<meta charset="utf-8">
<title>Stonegate Towing Business Card</title>
<link href="https://fonts.googleapis.com/css2?family=Montserrat:wght@500;700;800&display=swap" rel="stylesheet">
<style>
  :root {
    --stage: #3b3b3c;
    --card: #ffffff;
    --ink: #141414;
    --red: #d21f26;
    --text: #2a2a2a;
  }
  * { margin: 0; padding: 0; box-sizing: border-box; }
  html, body { width: 1200px; height: 689px; overflow: hidden; }
  body {
    background: var(--stage);
    font-family: "Montserrat", Arial, sans-serif;
    position: relative;
  }
  .card {
    position: absolute;
    top: 190px;
    width: 520px;
    height: 300px;
    background: var(--card);
    border-radius: 22px;
    overflow: hidden;
    box-shadow: 0 18px 40px rgba(0,0,0,.45);
  }
  .card--front { left: 50px; }
  .card--back { left: 630px; }

  .brand {
    font-weight: 800;
    color: var(--red);
    line-height: 1.05;
    text-transform: uppercase;
    letter-spacing: .02em;
  }
  .card--front .brand {
    position: absolute;
    inset: 0;
    display: flex;
    align-items: center;
    justify-content: center;
    text-align: center;
    padding: 40px 50px;
    font-size: 50px;
  }

  .back-panel {
    position: absolute;
    left: 0; top: 0;
    width: 200px; height: 300px;
  }
  .phone {
    position: absolute;
    left: 12px; top: 150px;
    transform-origin: left top;
    transform: rotate(-90deg) translate(-50%, 0);
    display: flex;
    align-items: center;
    gap: 10px;
    color: var(--red);
    font-weight: 800;
    font-size: 38px;
    white-space: nowrap;
  }
  .hours {
    position: absolute;
    left: 72px; top: 150px;
    transform-origin: left top;
    transform: rotate(-90deg) translate(-50%, 0);
    background: var(--card);
    color: var(--ink);
    border-radius: 14px;
    padding: 5px 18px;
    font-size: 13px;
    font-weight: 500;
    letter-spacing: .08em;
    white-space: nowrap;
  }

  .card--back .brand {
    position: absolute;
    left: 215px; right: 24px; top: 42px;
    font-size: 22px;
    white-space: nowrap;
  }
  .services {
    position: absolute;
    left: 215px; top: 108px;
    list-style: none;
  }
  .services li {
    display: flex;
    align-items: center;
    gap: 10px;
    font-size: 13.5px;
    font-weight: 500;
    color: var(--text);
    text-transform: uppercase;
    letter-spacing: .03em;
    height: 25px;
    white-space: nowrap;
  }
  .service-icon {
    width: 18px; height: 18px;
    border-radius: 4px;
    background: var(--red);
    opacity: .85;
    flex: none;
  }
</style>
</head>
<body>

  <section class="card card--front" aria-label="Card front">
    <div class="brand">Stonegate Towing</div>
  </section>

  <section class="card card--back" aria-label="Card back">
    <svg class="back-panel" viewBox="0 0 200 300" aria-hidden="true">
      <path d="M0 0 H110 C150 60 120 150 160 230 C175 262 190 285 200 300 H0 Z" fill="var(--red)"/>
      <path d="M0 0 H98 C138 60 110 150 148 232 C160 260 172 285 180 300 H0 Z" fill="var(--card)"/>
      <path d="M0 0 H92 C130 60 102 150 140 232 C152 260 162 285 170 300 H0 Z" fill="var(--ink)"/>
    </svg>

    <div class="phone">
      <svg width="28" height="28" viewBox="0 0 24 24" aria-hidden="true">
        <path fill="var(--red)" d="M6.6 10.8a15 15 0 0 0 6.6 6.6l2.2-2.2a1 1 0 0 1 1-.25 11.4 11.4 0 0 0 3.6.57 1 1 0 0 1 1 1V20a1 1 0 0 1-1 1A17 17 0 0 1 3 4a1 1 0 0 1 1-1h3.5a1 1 0 0 1 1 1c0 1.25.2 2.45.57 3.6a1 1 0 0 1-.25 1z"/>
      </svg>
      <span>7354 2618</span>
    </div>
    <div class="hours">24 HOUR BUSINESS 7 DAYS</div>

    <div class="brand">Stonegate Towing</div>

    <ul class="services">
      <li><span class="service-icon" role="img" aria-label="Tow truck icon"></span>Towing</li>
      <li><span class="service-icon" role="img" aria-label="Accident icon"></span>Accident Towing</li>
      <li><span class="service-icon" role="img" aria-label="Breakdown icon"></span>Mechanical Breakdown</li>
      <li><span class="service-icon" role="img" aria-label="Insurance shield icon"></span>Insurance, Salvage &amp; Recovery</li>
      <li><span class="service-icon" role="img" aria-label="Off road vehicle icon"></span>4WD Off Road Towing</li>
      <li><span class="service-icon" role="img" aria-label="Heavy truck icon"></span>Light &amp; Heavy Towing</li>
    </ul>
  </section>

</body>
</html>
```